Brantley Water Taxi and Transport

Need to redesign our business cards to relay that we do freight logistics and water taxi service. We also work with gov. agencies doing environmental clean up, oil spill response, remote site construction and work with many of the air taxi and helicopter services on Kodiak Island. Out website is www.brantleywatertaxi-example.com to get a better idea of what we do.

Contact Information for Business Card

I have a previous business card but it just has the logo on the front, and a sunset picture on the back with the contact info. It does not relay what we do and what we can help with. I like a simple straight forward design over a busy one.

Colors
3176b5
0455a3
cfdfed

Requirements
Must have
• logo, email, website, phone number

```html
<!DOCTYPE html>
<html lang="en">
<head>
<meta charset="utf-8">
<title>Brantley Water Taxi and Transport — Business Card</title>
<link rel="stylesheet" href="https://fonts.googleapis.com/css2?family=Montserrat:wght@400;500;700;800&display=swap">
<style>
  :root {
    --stage: #3b5478;
    --brand-blue: #0455a3;
    --card-blue: #1c4f97;
    --mid-blue: #3176b5;
    --pale-blue: #cfdfed;
    --panel-white: #ecf0f4;
    --sun-orange: #f0a23a;
    --ink-white: #ffffff;
  }
  * { box-sizing: border-box; margin: 0; padding: 0; }
  html, body { width: 1200px; height: 1000px; overflow: hidden; }
  body {
    background: var(--stage);
    font-family: "Montserrat", Arial, sans-serif;
    display: flex;
    flex-direction: column;
    align-items: center;
    justify-content: center;
    gap: 60px;
  }
  .card {
    position: relative;
    width: 700px;
    height: 400px;
    border-radius: 6px;
    overflow: hidden;
    box-shadow: 0 14px 30px rgba(0,0,0,0.3);
  }

  /* Front side */
  .card-front { background: var(--card-blue); }
  .front-brand-panel {
    position: absolute; left: 0; top: 0;
    width: 430px; height: 270px;
    background: var(--panel-white);
    display: flex; align-items: center; padding-left: 44px; gap: 18px;
  }
  .brand-dot {
    width: 44px; height: 44px; border-radius: 50%;
    background: var(--sun-orange); flex: none;
  }
  .brand-name {
    color: var(--brand-blue);
    font-weight: 800;
    line-height: 1.05;
  }
  .brand-name .line-main { display: block; font-size: 50px; letter-spacing: 1px; }
  .brand-name .line-sub { display: block; font-size: 20px; letter-spacing: 0.5px; margin-top: 4px; }

  .services {
    position: absolute; left: 458px; top: 36px;
    width: 220px;
    display: grid; grid-template-columns: 1fr; row-gap: 22px;
  }
  .service { display: flex; align-items: center; gap: 12px; }
  .service-icon {
    width: 34px; height: 24px; border-radius: 3px;
    background: var(--pale-blue); flex: none;
  }
  .service-label {
    color: var(--ink-white); font-size: 13px; font-weight: 500; line-height: 1.2;
  }

  .contact {
    position: absolute; left: 44px; bottom: 30px;
    list-style: none; color: var(--ink-white);
    font-size: 14px; line-height: 1.75;
  }
  .contact .label { color: var(--sun-orange); font-weight: 700; margin-right: 6px; }

  /* Back side */
  .card-back {
    background: var(--card-blue);
    display: flex; align-items: center; justify-content: center; gap: 22px;
  }
  .card-back .brand-name { color: var(--ink-white); }
  .card-back .brand-name .line-main { font-size: 60px; }
  .card-back .brand-name .line-sub { font-size: 24px; }
</style>
</head>
<body>

  <section class="card card-front" aria-label="Business card front">
    <div class="front-brand-panel">
      <span class="brand-dot" aria-hidden="true"></span>
      <h1 class="brand-name">
        <span class="line-main">BRANTLEY</span>
        <span class="line-sub">Water Taxi &amp; Transport</span>
      </h1>
    </div>

    <ul class="services" aria-label="Services">
      <li class="service"><span class="service-icon" role="img" aria-label="Water taxi boat icon"></span><span class="service-label">Water Taxi</span></li>
      <li class="service"><span class="service-icon" role="img" aria-label="Freight barge icon"></span><span class="service-label">Freight Transport</span></li>
      <li class="service"><span class="service-icon" role="img" aria-label="Oil spill vessel icon"></span><span class="service-label">Oil Spill Response</span></li>
      <li class="service"><span class="service-icon" role="img" aria-label="Construction cargo icon"></span><span class="service-label">Construction Transport</span></li>
      <li class="service"><span class="service-icon" role="img" aria-label="Emergency vessel icon"></span><span class="service-label">Emergency Response</span></li>
      <li class="service"><span class="service-icon" role="img" aria-label="Cleanup vessel icon"></span><span class="service-label">Environmental Cleanup</span></li>
    </ul>

    <ul class="contact" aria-label="Contact details">
      <li><span class="label">P:</span>555-014-2200</li>
      <li><span class="label">E:</span>hello@brantleywatertaxi-example.com</li>
      <li><span class="label">W:</span>www.brantleywatertaxi-example.com</li>
    </ul>
  </section>

  <section class="card card-back" aria-label="Business card back">
    <span class="brand-dot" aria-hidden="true"></span>
    <h2 class="brand-name">
      <span class="line-main">BRANTLEY</span>
      <span class="line-sub">Water Taxi &amp; Transport</span>
    </h2>
  </section>

</body>
</html>
```